Stationary for Marigold Spa
Business Card, Envelope, & Letterhead
Project: Stationary for Marigold Spa
Stationary for Marigold Spa -
Creative Brief
Simple
use logo no person's name
27815 Orchard Blvd. Ste 342 San Antonio, TX 78259
hbt4726@quillpost.net
We don't have the website yet. Please do not use the email on the project. On the business card front side, we only need our logo, address, phone no. Back side will be the services that we will provide.
Acupressure, Tui Na, Deep Tissue Massage, Swedish Massage, Prenatal Massage, Reflexology, Traditional Herbal Foot Treatment

```html
<!DOCTYPE html>
<html lang="en">
<head>
<meta charset="utf-8">
<title>Marigold Spa – Business Card</title>
<link rel="stylesheet" href="https://fonts.googleapis.com/css2?family=Questrial&display=swap">
<style>
  :root {
    --backdrop: #ecebe6;
    --card: #ffffff;
    --ink-grey: #7d7f82;
    --swoosh-grey: #b9babc;
    --olive: #b8bb22;
    --olive-dark: #9ea11a;
    --band-ink: #34360c;
  }
  html, body {
    margin: 0;
    padding: 0;
    width: 1200px;
    height: 780px;
    overflow: hidden;
    background: var(--backdrop);
  }
  .canvas {
    position: relative;
    width: 1200px;
    height: 780px;
  }
  .business-card {
    position: absolute;
    left: 100px;
    top: 100px;
    width: 1000px;
    height: 580px;
    background: var(--card);
    border-radius: 34px;
    overflow: hidden;
    box-shadow: 0 10px 30px rgba(0,0,0,0.18);
    font-family: "Questrial", "Century Gothic", sans-serif;
  }
  .card-bands {
    position: absolute;
    inset: 0;
  }
  .brand {
    position: absolute;
    left: 0;
    right: 0;
    top: 150px;
    text-align: center;
  }
  .brand-name {
    display: inline-flex;
    align-items: center;
    gap: 16px;
    font-size: 66px;
    color: var(--ink-grey);
    letter-spacing: -0.5px;
    line-height: 1;
  }
  .brand-dot {
    width: 18px;
    height: 18px;
    border-radius: 50%;
    background: var(--olive);
  }
  .tagline {
    margin-top: 8px;
    font-size: 28px;
    color: var(--olive-dark);
  }
  .phone {
    position: absolute;
    left: 0;
    right: 0;
    top: 300px;
    display: flex;
    justify-content: center;
    align-items: center;
    gap: 16px;
    font-size: 40px;
    color: var(--ink-grey);
  }
  .phone-icon { width: 42px; height: 42px; }
  .address {
    position: absolute;
    right: 44px;
    bottom: 30px;
    font-size: 23px;
    color: var(--band-ink);
    letter-spacing: 0.2px;
  }
</style>
</head>
<body>
<div class="canvas">
  <div class="business-card">
    <svg class="card-bands" viewBox="0 0 1000 580" preserveAspectRatio="none" aria-hidden="true">
      <path fill="var(--swoosh-grey)" d="M0,425 C320,470 650,385 1000,300 L1000,322 C650,410 320,492 0,447 Z"/>
      <path fill="var(--olive)" d="M0,472 C320,508 660,432 1000,350 L1000,580 L0,580 Z"/>
    </svg>

    <div class="brand">
      <div class="brand-name"><span class="brand-dot"></span>Marigold Spa</div>
      <div class="tagline">Health Relaxation</div>
    </div>

    <div class="phone">
      <svg class="phone-icon" viewBox="0 0 42 42" aria-hidden="true">
        <circle cx="21" cy="21" r="18.5" fill="none" stroke="var(--olive)" stroke-width="3"/>
        <path fill="var(--olive)" d="M15.5 11.5c1-.6 2-.3 2.5.6l1.8 3.3c.4.8.2 1.7-.5 2.2l-1.3 1c.9 2.2 2.5 4 4.6 5.1l1.1-1.2c.6-.7 1.5-.8 2.3-.4l3.2 2c.8.5 1 1.6.4 2.4l-1.4 1.9c-.8 1-2.1 1.4-3.3 1-5.5-1.8-9.6-6.2-11.1-11.8-.3-1.2.2-2.5 1.2-3.2z"/>
      </svg>
      <span class="phone-number">(210)555-0147</span>
    </div>

    <div class="address">27815 Orchard Blvd. Ste 342 San Antonio, TX 78259</div>
  </div>
</div>
</body>
</html>
```